Bright Album Android app screenshots

I need some screenshot backgrounds that will be used as a background for Bright Album at https://apps.quorvane.com/store/apps/details?id=com.brightpocketkit.album&hl=en-GB . I want to replace that boring orange background with something more exciting, maybe put some icons related to galleries there. Something like https://apps.quorvane.com/store/apps/details?id=com.brightpocketkit.calendar&hl=en-US has been done for the calendar. Let's keep it orange #F57C00 though and the resolution should be 2000x3555, I need 4 slightly different variants. Only the top and the sides of the background will be visible so focus on those parts. I need only the orange backgrounds, not the actual device or screenshot itself.

```html
<!DOCTYPE html>
<html lang="en">
<head>
<meta charset="utf-8">
<title>Bright Album — Screenshot Background</title>
<style>
  :root {
    --orange-base: #FF8A00;
    --orange-deep: #FF8000;
    --orange-mid: #FF9200;
    --orange-light: #FF9A00;
    --orange-bright: #FFA200;
    --orange-icon: #FF7A00;
    --icon-white: #FFFFFF;
  }
  html, body {
    margin: 0;
    padding: 0;
    width: 675px;
    height: 1200px;
    overflow: hidden;
    background: var(--orange-base);
  }
  .backdrop {
    position: relative;
    width: 675px;
    height: 1200px;
    overflow: hidden;
  }
  .backdrop__art {
    display: block;
    width: 675px;
    height: 1200px;
  }
  .icon-line {
    fill: none;
    stroke: var(--icon-white);
    stroke-width: 6;
    stroke-linecap: round;
    stroke-linejoin: round;
  }
  .icon-camera {
    fill: none;
    stroke: var(--orange-icon);
    stroke-width: 55;
    stroke-linecap: round;
    stroke-linejoin: round;
  }
  .icon-camera__flash { fill: var(--orange-icon); }
  .icon-soft { opacity: 0.75; }
</style>
</head>
<body>
<main class="backdrop">
  <svg class="backdrop__art" viewBox="0 0 1449 2576" preserveAspectRatio="none" aria-hidden="true">
    <defs>
      <linearGradient id="base-fill" x1="0" y1="0" x2="1" y2="0">
        <stop offset="0" stop-color="#FF8C00"/>
        <stop offset="1" stop-color="#FF8000"/>
      </linearGradient>
      <linearGradient id="blob-top-left" x1="0" y1="0" x2="0" y2="1">
        <stop offset="0" stop-color="#FF9500"/>
        <stop offset="1" stop-color="#FFA300"/>
      </linearGradient>
      <linearGradient id="blob-lower" x1="0" y1="0" x2="0" y2="1">
        <stop offset="0" stop-color="#FF9800"/>
        <stop offset="1" stop-color="#FF9B00"/>
      </linearGradient>
      <filter id="soft-blur" x="-20%" y="-20%" width="140%" height="140%">
        <feGaussianBlur stdDeviation="4"/>
      </filter>
    </defs>

    <!-- base -->
    <rect class="bg-base" width="1449" height="2576" fill="url(#base-fill)"/>

    <!-- top-right blob -->
    <path class="blob blob--top-right" fill="#FF8E00"
      d="M1449 190 C1150 170 960 420 915 700 C885 880 890 1000 890 1010 L1449 1030 Z"/>

    <!-- middle arch -->
    <path class="blob blob--middle" fill="#FF8D00" opacity="0.9"
      d="M420 1040 C560 780 700 660 920 620 C1150 590 1330 630 1449 680 L1449 1030 C1100 1040 900 1000 740 1005 C600 1005 500 1020 420 1040 Z"/>

    <!-- top-left blob -->
    <path class="blob blob--top-left" fill="url(#blob-top-left)"
      d="M0 0 L360 0 C420 90 520 170 560 250 C600 340 607 400 607 450 C607 760 380 1000 0 1052 Z"/>

    <!-- lower field -->
    <path class="blob blob--lower" fill="url(#blob-lower)"
      d="M0 1340 C150 1100 420 1005 740 1005 C1000 1005 1200 1040 1449 1025 L1449 2576 L0 2576 Z"/>

    <!-- lower-left tongue -->
    <path class="blob blob--lower-left" fill="#FF8C00"
      d="M0 1640 C150 1830 240 2100 240 2300 C240 2420 220 2520 210 2576 L0 2576 Z"/>

    <!-- sweep from centre down -->
    <path class="blob blob--sweep" fill="#FF9600" opacity="0.6"
      d="M890 1010 C900 1400 920 1700 820 2050 C720 2380 520 2500 340 2576 L290 2576 C280 2200 290 1700 330 1400 C360 1200 390 1120 420 1040 C600 1010 760 1005 890 1010 Z"/>

    <!-- gallery icon, crisp -->
    <g class="icon-gallery" transform="translate(125 390) rotate(-15)">
      <rect class="icon-line" x="-135" y="-92" width="262" height="184" rx="18"/>
      <circle class="icon-line" cx="28" cy="-34" r="21"/>
      <polyline class="icon-line" points="-132,72 -82,-18 38,40"/>
      <polyline class="icon-line" points="6,92 48,10 124,52"/>
    </g>

    <!-- gallery icon, soft -->
    <g class="icon-gallery icon-soft" filter="url(#soft-blur)" transform="translate(1060 40) rotate(-15)">
      <rect class="icon-line" x="-120" y="-100" width="245" height="175" rx="18"/>
      <circle class="icon-line" cx="28" cy="-40" r="20"/>
      <polyline class="icon-line" points="-118,55 -72,-30 40,30"/>
      <polyline class="icon-line" points="0,75 44,-5 122,45"/>
    </g>

    <!-- camera icon, large -->
    <g class="icon-camera-group">
      <path class="icon-camera"
        d="M20 2190 L40 2140 Q65 2085 125 2108 L400 2210 Q455 2235 440 2292 L420 2350 L612 2418 Q690 2450 668 2532 L640 2610"/>
      <circle class="icon-camera" cx="115" cy="2610" r="245"/>
      <circle class="icon-camera__flash" cx="520" cy="2500" r="50"/>
    </g>

    <!-- camera icon, soft -->
    <g class="icon-camera-soft icon-soft" filter="url(#soft-blur)" transform="translate(1440 2390) rotate(-15)">
      <path class="icon-line" d="M-90 -55 L-55 -60 L-50 -80 Q-45 -95 -25 -95 L90 -95 L90 95 L-80 95 Q-95 95 -98 80 L-98 -45 Q-98 -55 -90 -55 Z"/>
      <circle class="icon-line" cx="10" cy="10" r="40"/>
    </g>
  </svg>
</main>
</body>
</html>
```